Business card design for engineering firm specializing in defense industry.

We need a professional business card design. Something simple but stands out. We are an engineering company specializing in composites in the defense industry.
Industry/Entity Type
Defense
Contact Information for Business Card
A simple black business card with the Fibrolane yellow color is what we had in mind but open for other designs.
Colors
ffc214

```html
<!DOCTYPE html>
<html lang="en">
<head>
<meta charset="utf-8">
<title>Fibrolane Business Card</title>
<link rel="stylesheet" href="https://fonts.googleapis.com/css2?family=Oswald:wght@300;400;500&display=swap">
<style>
  :root {
    --page: #f4f4f4;
    --card: #272324;
    --brand-yellow: #ffc214;
    --white: #ffffff;
    --front-name: #5a5859;
  }
  * { margin: 0; padding: 0; box-sizing: border-box; }
  html, body {
    width: 1200px; height: 900px; overflow: hidden;
    background: var(--page);
    font-family: "Oswald", sans-serif;
  }
  .canvas { position: relative; width: 1200px; height: 900px; }
  .card {
    position: absolute; background: var(--card); overflow: hidden;
  }
  .card-front { left: 306px; top: 97px; width: 587px; height: 335px; }
  .card-back { left: 306px; top: 466px; width: 585px; height: 334px; }

  .front-wordmark {
    position: absolute; left: 47px; top: 140px;
    font-size: 40px; font-weight: 500; letter-spacing: 0.5px;
    color: var(--front-name); line-height: 1;
  }
  .front-block {
    position: absolute; left: 360px; top: 108px; width: 118px; height: 118px;
    background: linear-gradient(135deg, #1c1a1b 0%, #2f2d2e 60%, #4a4849 100%);
  }

  .back-wordmark {
    position: absolute; left: 34px; top: 52px;
    display: flex; align-items: center; gap: 12px;
  }
  .back-wordmark .name {
    font-size: 40px; font-weight: 500; color: var(--white); line-height: 1;
  }
  .back-wordmark .mark-square {
    width: 14px; height: 14px; background: var(--brand-yellow);
  }

  .person { position: absolute; right: 33px; top: 54px; text-align: right; }
  .person-name { font-size: 28px; font-weight: 500; color: var(--white); line-height: 1.1; letter-spacing: 0.3px; }
  .person-title { font-size: 14px; font-weight: 300; color: var(--brand-yellow); line-height: 1.4; }

  .divider {
    position: absolute; left: 34px; top: 189px; width: 518px; height: 2px;
    background: linear-gradient(to right, var(--white) 0 330px, var(--brand-yellow) 330px);
  }
  .divider::after {
    content: ""; position: absolute; left: 330px; right: 0; top: 0; height: 1px; background: var(--card);
  }

  .contacts { position: absolute; left: 34px; top: 222px; list-style: none; }
  .contacts li {
    display: flex; align-items: center; gap: 11px;
    font-size: 17px; font-weight: 300; color: var(--white); height: 24px;
  }
  .contacts svg { width: 17px; height: 17px; fill: var(--brand-yellow); flex: none; }
  .accent { color: var(--brand-yellow); }

  .address {
    position: absolute; right: 33px; top: 222px;
    display: flex; gap: 9px; align-items: flex-start;
  }
  .address-text {
    text-align: right; font-size: 17px; font-weight: 300; color: var(--white); line-height: 24px;
  }
  .address svg { width: 14px; height: 18px; fill: var(--brand-yellow); margin-top: 4px; }

  .base-band {
    position: absolute; left: 0; right: 0; bottom: 0; height: 12px; background: var(--brand-yellow);
  }
</style>
</head>
<body>
<main class="canvas">
  <section class="card card-front" aria-label="Card front">
    <div class="front-wordmark">Fibrolane</div>
    <div class="front-block"></div>
  </section>

  <section class="card card-back" aria-label="Card back">
    <div class="back-wordmark">
      <span class="name">Fibrolane</span>
      <span class="mark-square"></span>
    </div>

    <div class="person">
      <div class="person-name">Marcus Hale</div>
      <div class="person-title">President &amp; CEO</div>
    </div>

    <div class="divider"></div>

    <ul class="contacts">
      <li>
        <svg viewBox="0 0 24 24" aria-hidden="true"><path d="M6.6 10.8a15.1 15.1 0 0 0 6.6 6.6l2.2-2.2c.3-.3.7-.4 1-.2 1.1.4 2.3.6 3.6.6.6 0 1 .4 1 1V20c0 .6-.4 1-1 1A17 17 0 0 1 3 4c0-.6.4-1 1-1h3.5c.6 0 1 .4 1 1 0 1.3.2 2.5.6 3.6.1.3 0 .7-.2 1z"/></svg>
        <span>0475 312 940</span>
      </li>
      <li>
        <svg viewBox="0 0 24 24" aria-hidden="true"><path d="M2 5h20v14H2z M3.5 6.5 12 13l8.5-6.5" stroke="#272324" stroke-width="1.6"/></svg>
        <span>info@fibrolane.com</span>
      </li>
      <li>
        <svg viewBox="0 0 24 24" aria-hidden="true"><circle cx="12" cy="12" r="10"/><path d="M8 6l3 2-1 3-3 1-1 3M14 14l3 1 1 3-2 2M15 4l-1 3 3 1" stroke="#272324" stroke-width="1.6" fill="none"/></svg>
        <span>www.<span class="accent">fibrolane</span>.com</span>
      </li>
    </ul>

    <div class="address">
      <div class="address-text">214&nbsp; Ashgrove Lane, Cedar Falls<br>27530, North Carolina</div>
      <svg viewBox="0 0 14 18" aria-hidden="true"><path d="M7 0a7 7 0 0 1 7 7c0 5-7 11-7 11S0 12 0 7a7 7 0 0 1 7-7zm0 4.3a2.7 2.7 0 1 0 0 5.4 2.7 2.7 0 0 0 0-5.4z"/></svg>
    </div>

    <div class="base-band"></div>
  </section>
</main>
</body>
</html>
```